The Quiet Harbor

I have a faux cover I will attach & want you to follow & enhance what I've created. Just an FYI, the book will be posted on brindlo & I'm working with Marrow Lane Publishing.
What you need to know:
The dimensions: 6" x 9" (15.24 x 22.86 cm)
Background color: Black
I did not capture the color of the font, so want you to get a similar gold color.
Font for title, subtitle & author name: Goudy Old Style
Font for "20th Anniversary Edition": Kunstler Script
I have thoughts of shaping the photo in an oval shape -- possibly shade out the edges?

Target Market(s)

All ages: anyone who has encountered issues with doctors, hospitals, and especially those who have struggled with cancer treatment.

Requirements
Nice to have
• Adding below another PDF, showing vintage lines that I would like to see used. Just added some text I will add to the back cover. I am waiting on one more review, which I will add. Attaching that below.

```html
<!DOCTYPE html>
<html lang="en">
<head>
<meta charset="UTF-8">
<title>The Quiet Harbor — Joan Rourke</title>
<link rel="stylesheet" href="https://fonts.googleapis.com/css2?family=Sorts+Mill+Goudy:ital@0;1&family=Pinyon+Script&display=swap">
<style>
  :root {
    --cover-bg: #363636;
    --gold: #ffc961;
    --gold-glow: rgba(255, 226, 170, 0.45);
    --photo-light: #e4e5ea;
    --photo-mid: #9c9ca2;
    --photo-dark: #3f3f42;
  }
  html, body {
    margin: 0;
    padding: 0;
    width: 800px;
    height: 1200px;
    overflow: hidden;
    background: var(--cover-bg);
  }
  .cover {
    position: relative;
    width: 800px;
    height: 1200px;
    background: var(--cover-bg);
    color: var(--gold);
    font-family: "Sorts Mill Goudy", "Goudy Old Style", serif;
    text-align: center;
  }
  .cover-title {
    position: absolute;
    top: 94px;
    left: 0;
    width: 100%;
    margin: 0;
    font-size: 66px;
    font-weight: 400;
    letter-spacing: 0;
    line-height: 1;
    white-space: nowrap;
    -webkit-text-stroke: 1.4px var(--gold);
  }
  .cover-subtitle {
    position: absolute;
    top: 176px;
    left: 20px;
    width: 760px;
    margin: 0;
    font-style: italic;
    font-size: 33px;
    line-height: 51px;
    white-space: nowrap;
    -webkit-text-stroke: 1px var(--gold);
  }
  .cover-edition {
    position: absolute;
    top: 300px;
    left: 0;
    width: 100%;
    margin: 0;
    font-family: "Pinyon Script", cursive;
    font-size: 66px;
    font-weight: 400;
    line-height: 1.2;
    white-space: nowrap;
  }
  .cover-edition sup {
    font-size: 34px;
    vertical-align: 28px;
    margin-left: -4px;
    margin-right: 6px;
  }
  .portrait-oval {
    position: absolute;
    left: 164px;
    top: 435px;
    width: 472px;
    height: 588px;
    border-radius: 50%;
    background:
      radial-gradient(ellipse 38% 34% at 50% 44%, #8a8a8f 0%, #6f6f74 60%, transparent 100%),
      linear-gradient(180deg, var(--photo-light) 0%, #cfd0d6 45%, var(--photo-mid) 62%, var(--photo-dark) 100%);
    box-shadow: 0 0 26px 6px var(--gold-glow);
  }
  .cover-author {
    position: absolute;
    top: 1062px;
    left: 0;
    width: 100%;
    margin: 0;
    font-size: 74px;
    font-weight: 400;
    line-height: 1;
    white-space: nowrap;
    -webkit-text-stroke: 1.4px var(--gold);
  }
</style>
</head>
<body>
  <main class="cover">
    <h1 class="cover-title">THE QUIET HARBOR</h1>
    <p class="cover-subtitle">A tale of lifelong damage from terminal cancer<br>“treatment” &amp; inhumane doctors</p>
    <p class="cover-edition">20<sup>th</sup> Anniversary Edition</p>
    <div class="portrait-oval" role="img" aria-label="Black-and-white oval portrait photograph of the author, softly vignetted with a warm glow at the edges"></div>
    <p class="cover-author">Joan Rourke</p>
  </main>
</body>
</html>
```